Modern & Simple Essential Oils Label

Company Name: Meadowlark Essentials

What we sell: Aromatherapy products, pure therapeutic essential oils.

Design need:
We are looking for a creative and youthful design for the labels used on small essentials oils.

I have two sizes of bottles that I use for essential oils a 5ml bottle and a 15ml bottle. They are dark Amber color glass with black lids. I like the clear labels or mayble a dark brown background. With white or clear lettering with punch of color too! Each oil type is represented by different color. (lavender- purple, lemon - yellow). The label will be the same for all the oils in the two sizes with only a different oil name & coordinating color.
5ml label size should be: 1 " x 2.625"
15ml label size should be: 1.5" x 3.5"

I have some labels that I have had another designer start on, but they aren't quite what I want and missing that something (alot!).. I don't know what. Interest maybe? Lack of design? I dunno.. they are attached. Maybe it's the logo? I don't know! But its gotta change! When I cut out a proof and put a sample on the bottle as I look straight on at the label all I see is a big dot, no logo.. nothing interesting.
Updates

Project Deadline Extended
Reason: Hi! Id like to extend this deadline. Ive been unavailable for a few days due to an illness and Im so far behind! Im feeling MUCH better and looking forward to getting caught up and move with the project. Im not sure how this works, but I attached a list of the oils that we currently have available. And in the list is the idea for the color schemes for the oils. The basic idea is for it to have a wide array of colors, so using different shades of greens, yellows, oranges and so on. So that its like a rainbow. We are not set of that particular color for that particular oil. It was just a idea list of possible colors for oils. Thanks so much!

Target Market(s)

Metro & Modern people. Interested in healthy organic living, Mostly women (some men) 20-45 who are interested in holistic healing.

Industry/Entity Type

It Company

Requirements
Must have
• A reputable look. Clean, organic, crisp, zen or spa-like feel. Modern, youthful appealing label design. Approachable and interesting, not intimidating so that I don't turn away people who are new or not familiar with how to use essential oils.
Should not have
• do NOT want the look to be anywhere close to medicinal, witchy, crafty, hippie, mystical, overly earthy, magical, or voodoo. Do not want it to look like something out of a grandmothers medicine cabinet.

```html
<!DOCTYPE html>
<html lang="en">
<head>
<meta charset="utf-8">
<title>Meadowlark Essentials – Basil 15 ml Label</title>
<link href="https://fonts.googleapis.com/css2?family=Roboto+Condensed:wght@400;700&family=Open+Sans:ital,wght@1,700&family=Yellowtail&family=Raleway:wght@300&display=swap" rel="stylesheet">
<style>
  :root {
    --page: #ffffff;
    --label: #eeecec;
    --leaf: #3aaa35;
    --ink: #8c8c8c;
    --ink-strong: #7a7a7a;
    --trim: #555555;
    --white: #ffffff;
  }
  * { margin: 0; padding: 0; box-sizing: border-box; }
  html, body { width: 1200px; height: 591px; overflow: hidden; background: var(--page); }
  .canvas { position: relative; width: 1200px; height: 591px; }

  .trim-mark { position: absolute; left: 599px; width: 1px; height: 24px; background: var(--trim); }
  .trim-mark--top { top: 45px; }
  .trim-mark--bottom { top: 521px; }

  .label { position: absolute; left: 75px; top: 69px; width: 1050px; height: 452px; background: var(--label); }

  /* Back panel: content set sideways, reading bottom to top */
  .back-panel {
    position: absolute; left: 75px; top: 521px;
    width: 452px; height: 525px;
    transform-origin: top left; transform: rotate(-90deg);
    font-family: "Roboto Condensed", "Arial Narrow", sans-serif;
    color: var(--ink); font-size: 16.5px; line-height: 24px;
  }
  .facts-box {
    position: absolute; left: 11px; top: 15px; width: 422px; height: 162px;
    border: 3px solid var(--leaf);
  }
  .facts-title { position: absolute; left: 14px; top: 10px; font-size: 21px; font-weight: 700; color: var(--ink-strong); }
  .facts-list { position: absolute; left: 14px; top: 38px; list-style: none; line-height: 22px; }
  .facts-band {
    position: absolute; left: -3px; bottom: -3px; width: 422px; height: 32px;
    background: var(--leaf); color: var(--white);
    padding-left: 17px; line-height: 32px; font-size: 17px;
  }
  .company { position: absolute; left: 11px; top: 189px; }
  .usage { position: absolute; left: 11px; top: 256px; width: 440px; }
  .caution { position: absolute; left: 11px; top: 346px; width: 445px; }
  .caution strong { font-weight: 700; color: var(--ink-strong); }

  /* Front panel */
  .botanical-name {
    position: absolute; left: 935px; top: 114px;
    font-family: "Open Sans", Arial, sans-serif; font-style: italic; font-weight: 700;
    font-size: 20px; line-height: 28px; color: var(--ink); text-transform: uppercase;
  }
  .oil-name {
    position: absolute; left: 640px; top: 205px;
    font-family: "Yellowtail", cursive; font-size: 190px; line-height: 1;
    color: var(--leaf); letter-spacing: 4px;
  }
  .volume {
    position: absolute; left: 612px; top: 478px; width: 80px; height: 40px;
    transform-origin: top left; transform: rotate(-90deg) translate(-40px, 0);
    font-family: "Roboto Condensed", Arial, sans-serif; font-weight: 700;
    font-size: 28px; color: var(--leaf); line-height: 40px;
  }
  .brand-band {
    position: absolute; left: 657px; top: 438px; width: 466px; height: 81px;
    background: var(--leaf);
    display: flex; align-items: center; justify-content: center; gap: 10px;
  }
  .brand-dot { width: 9px; height: 9px; border-radius: 50%; background: var(--white); }
  .brand-name {
    font-family: "Raleway", sans-serif; font-weight: 300;
    font-size: 32px; color: var(--white); letter-spacing: 0.5px;
  }
</style>
</head>
<body>
<div class="canvas">
  <div class="trim-mark trim-mark--top"></div>
  <div class="trim-mark trim-mark--bottom"></div>
  <div class="label"></div>

  <section class="back-panel">
    <div class="facts-box">
      <h2 class="facts-title">Supplemental Facts</h2>
      <ul class="facts-list">
        <li>Serving Size: 1 drop</li>
        <li>Servings Per Container: About 250</li>
        <li>Oil: Rosmarinus Officinalis</li>
      </ul>
      <div class="facts-band">100% Pure Therapeutic Grade</div>
    </div>
    <p class="company">Meadowlark Essentials<br>P.O. Box 402, Brookfield, UT 84990</p>
    <p class="usage">For aromatic, topical use. 100% pure<br>therapeutic-grade essential oil. Dilute with a<br>carrier oil before using.</p>
    <p class="caution"><strong>CAUTION</strong>: For External Use Only. Not for<br>Ingestion. Keep away from eyes and mucous<br>membranes. May cause skin sensitivity. If<br>pregnant consult physician before use. Keep<br>out of reach of children. Keep away from flame.</p>
  </section>

  <p class="botanical-name">Ocimum<br>Basilicum<br>100% Pure<br>Essential Oil</p>
  <h1 class="oil-name">Basil</h1>
  <div class="volume">15 ml</div>
  <div class="brand-band">
    <span class="brand-dot"></span>
    <span class="brand-name">Meadowlark Essentials</span>
  </div>
</div>
</body>
</html>
```